HORIZON - and teamwork crafts of today

I´m writing a book about CHANGE and the skills leaders needs to embody the transformation from being amanager to become leaders.
The title of the book in Icelandic is the same as the name of the project (which I want to be used on the designes is:) SKÝJAFAR
(with the subtitle:) og hugrekkislist samtímans

Change is not controlled or managed – Leading effective change is an art form which is one of the big reasons for why 70% of changes within companies fail. The main reason however, is that managers are tasked with managing and directing them. The art form of change is to put it in the hands of leaders who possess the emotional intelligence that is needed – all their other advantages intact – to lead change all the way.

The big problem when it comes to change is that there are too many managers and too few leaders within companies – leaders who possess emotional intelligence which is the most important skill a leader embodies to empower change. A leader has what it takes to empower followership.

A manager tends to push and control, make decisions that he presupposes others to implement the way he expects. An emotionally competent leader leads by example and enhances followership on that journey because of the trust and respect he has earned.

In few words: SOFT SKILLS ARE THE NEW HARD SKILLS!

```html
<!DOCTYPE html>
<html lang="is">
<head>
<meta charset="utf-8">
<title>Skýjafar – og hugrekkislist samtímans</title>
<link rel="stylesheet" href="https://fonts.googleapis.com/css2?family=Arimo:wght@400;700&family=Tinos:ital,wght@1,700&display=swap">
<style>
  :root {
    --page: #ffffff;
    --cover: #ff4a05;
    --ghost: #ff6b33;
    --cream: #f8f5ea;
    --accent: #ffc400;
    --tape: #e8e6e3;
    --tape-edge: #d7d4d0;
    --ink-light: #ffffff;
  }
  html, body {
    margin: 0;
    padding: 0;
    width: 1200px;
    height: 1200px;
    overflow: hidden;
    background: var(--page);
  }
  .book-cover {
    display: block;
    width: 1200px;
    height: 1200px;
  }
  .cover-panel { fill: var(--cover); }
  .bonus-rule { stroke: var(--ink-light); stroke-width: 2; }
  .bonus-label {
    font-family: "Arimo", sans-serif;
    font-weight: 700;
    font-size: 29px;
    letter-spacing: -1px;
    fill: var(--accent);
  }
  .bonus-title {
    font-family: "Arimo", sans-serif;
    font-weight: 400;
    font-size: 29px;
    letter-spacing: -1px;
    fill: var(--ink-light);
  }
  .bonus-author {
    font-family: "Tinos", serif;
    font-style: italic;
    font-weight: 700;
    font-size: 22px;
    fill: var(--ink-light);
  }
  .title-ghost,
  .title-main {
    font-family: "Arimo", sans-serif;
    font-weight: 700;
    font-size: 152px;
    letter-spacing: -8px;
  }
  .title-ghost { fill: var(--ghost); }
  .title-main { fill: var(--cream); }
  .tape { fill: var(--tape); }
  .tape-edge { fill: var(--tape-edge); opacity: 0.7; }
  .subtitle-word {
    font-family: "Arimo", sans-serif;
    font-weight: 700;
    font-size: 108px;
    letter-spacing: -4px;
    fill: var(--cover);
  }
</style>
</head>
<body>
<svg class="book-cover" viewBox="0 0 1200 1200" xmlns="http://www.w3.org/2000/svg">
  <defs>
    <clipPath id="cover-clip">
      <rect x="228" y="0" width="800" height="1200"/>
    </clipPath>
  </defs>

  <rect class="cover-panel" x="228" y="0" width="800" height="1200"/>

  <g class="bonus-block">
    <line class="bonus-rule" x1="479" y1="85" x2="479" y2="178"/>
    <text class="bonus-label" x="504" y="108" textLength="266" lengthAdjust="spacingAndGlyphs">BONUS ARTICLE</text>
    <text class="bonus-title" x="486" y="152" textLength="502" lengthAdjust="spacingAndGlyphs">“ When Bosses Learn to Lead ”</text>
    <text class="bonus-author" x="975" y="188" text-anchor="end">Daniel R. Hartwell</text>
  </g>

  <g class="title-block" clip-path="url(#cover-clip)">
    <text class="title-ghost" x="236" y="440" textLength="810" lengthAdjust="spacingAndGlyphs">Skýjafar</text>
    <text class="title-main" x="236" y="515" textLength="810" lengthAdjust="spacingAndGlyphs">Skýjafar</text>
  </g>

  <g class="subtitle-tapes" clip-path="url(#cover-clip)">
    <polygon class="tape" points="228,676 452,632 463,744 228,790"/>
    <polygon class="tape-edge" points="440,634 452,632 463,744 450,746"/>
    <text class="subtitle-word" x="272" y="752" transform="rotate(-11 272 752)" textLength="150" lengthAdjust="spacingAndGlyphs">Og</text>

    <polygon class="tape" points="228,800 966,661 979,768 228,911"/>
    <polygon class="tape-edge" points="952,664 966,661 979,768 965,771"/>
    <text class="subtitle-word" x="282" y="900" transform="rotate(-10.6 282 900)" textLength="645" lengthAdjust="spacingAndGlyphs">Hugrekkislist</text>

    <polygon class="tape" points="228,976 806,861 816,965 228,1094"/>
    <polygon class="tape-edge" points="793,864 806,861 816,965 803,968"/>
    <text class="subtitle-word" x="282" y="1062" transform="rotate(-11 282 1062)" textLength="480" lengthAdjust="spacingAndGlyphs">Samtímans</text>
  </g>
</svg>
</body>
</html>
```